Bright Horizon Painting and Remodeling needs a business card

Business card should have company logo. I will upload two different logos and let me see which one is a better design for the business card.

Name of company: Bright Horizon Painting and Remodeling
Address: 4126 NW 71st st Suite 214
Miami, FL 33166

local phone: (305) 555-0142
toll free (855) 555-0197
fax (866) 555-0163

email: corinne@paintingbrighthorizon.example

not sure if i should include social media links or names on the business card.

company does interior and exterior painting, pressure washing, wall paper removal, drywall and stucco repair, staining,

We give free estimates.

I want a two sided business card.

Not sure if all this information is necessary for the business card. Designer can pick out whatever information they deem is important for a consumer to see on the business card.

Anticipating on the business card to be printed on nice quality.

I will upload an image of one of the logos on a type of business card surface. That idea can be used as well. Be creative. Business card should be professional but very nice and eye catching.

remove drywall and stucco repair and replace with tile installation

Industry/Entity Type

Business

Contact Information for Business Card

Miami, FL 33166

toll free (855) 555-0197
fax (866) 555-0163

company does interior and exterior painting, pressure washing, wall paper removal, drywall and stucco repair, staining, tile removal, *specializing in vinyl floor removal

free estimates.

Requirements
Must have
• Profesional font

```html
<!DOCTYPE html>
<html lang="en">
<head>
<meta charset="utf-8">
<title>Bright Horizon Painting and Remodeling – Business Card</title>
<link href="https://fonts.googleapis.com/css2?family=EB+Garamond:ital,wght@0,400;0,600;1,400&display=swap" rel="stylesheet">
<style>
  :root {
    --backdrop: #2b2b2b;
    --card: #fbfbfb;
    --ink: #4a4a4a;
    --ink-strong: #3a3a3a;
    --star: #e0403f;
    --orange: #f08a3c;
    --pink: #ef7aa0;
    --purple: #9a64c4;
    --blue: #4e8fd0;
    --teal: #3fb3b5;
    --green: #7cc24a;
    --yellow: #f2d843;
    --gold: #f0b73a;
  }
  * { box-sizing: border-box; margin: 0; padding: 0; }
  html, body { width: 1200px; height: 900px; overflow: hidden; }
  body {
    background: var(--backdrop);
    font-family: "EB Garamond", Georgia, serif;
    color: var(--ink);
    position: relative;
  }
  .card {
    position: absolute;
    left: 270px;
    width: 660px;
    height: 377px;
    background: var(--card);
    box-shadow: 0 12px 30px rgba(0,0,0,.45);
    overflow: hidden;
  }
  .card--front { top: 50px; }
  .card--back { top: 473px; }
  .card__stripes { position: absolute; inset: 0; width: 100%; height: 100%; }
  .brand {
    position: absolute;
    display: flex;
    align-items: center;
    gap: 12px;
  }
  .brand__dot {
    width: 34px; height: 34px; border-radius: 50%;
    background: var(--gold);
    flex: none;
  }
  .brand__name {
    font-weight: 600;
    font-size: 21px;
    line-height: 1.15;
    color: var(--ink-strong);
    max-width: 260px;
  }
  .card--front .brand { left: 56px; top: 70px; }
  .card--back .brand { left: 56px; top: 96px; }
  .services {
    position: absolute;
    left: 56px; top: 182px;
    list-style: none;
    font-size: 19px;
    line-height: 1.3;
  }
  .services li::before {
    content: "\2605";
    color: var(--star);
    margin-right: 10px;
    font-size: 15px;
  }
  .services__note {
    position: absolute;
    left: 56px; top: 318px;
    font-size: 22px;
    font-style: italic;
  }
  .contact {
    position: absolute;
    list-style: none;
    font-size: 18px;
    line-height: 1.45;
  }
  .contact li { display: flex; align-items: center; gap: 9px; }
  .contact svg { width: 15px; height: 15px; flex: none; }
  .contact--phones { left: 56px; top: 262px; }
  .contact--web { left: 300px; top: 262px; }
</style>
</head>
<body>

<section class="card card--front" aria-label="Card front">
  <svg class="card__stripes" viewBox="0 0 660 377" aria-hidden="true">
    <g fill="none" stroke-width="1.6">
      <line x1="560" y1="0" x2="660" y2="170" stroke="var(--orange)"/>
      <line x1="566" y1="0" x2="660" y2="160" stroke="var(--pink)"/>
      <line x1="572" y1="0" x2="660" y2="150" stroke="var(--purple)"/>
      <line x1="578" y1="0" x2="660" y2="140" stroke="var(--blue)"/>
      <line x1="584" y1="0" x2="660" y2="130" stroke="var(--teal)"/>
      <line x1="590" y1="0" x2="660" y2="120" stroke="var(--green)"/>
      <line x1="596" y1="0" x2="660" y2="110" stroke="var(--yellow)"/>
    </g>
  </svg>
  <div class="brand">
    <span class="brand__dot"></span>
    <span class="brand__name">Bright Horizon Painting and Remodeling</span>
  </div>
  <ul class="services">
    <li>Interior And Exterior Painting</li>
    <li>Pressure Washing</li>
    <li>Wall Paper Removal</li>
    <li>Drywall And Stucco Repair</li>
    <li>Staining</li>
  </ul>
  <p class="services__note">We Give Free Estimates.</p>
</section>

<section class="card card--back" aria-label="Card back">
  <svg class="card__stripes" viewBox="0 0 660 377" aria-hidden="true">
    <g fill="none" stroke-width="1.6">
      <line x1="470" y1="0" x2="660" y2="300" stroke="var(--orange)"/>
      <line x1="477" y1="0" x2="660" y2="289" stroke="var(--pink)"/>
      <line x1="484" y1="0" x2="660" y2="278" stroke="var(--purple)"/>
      <line x1="491" y1="0" x2="660" y2="267" stroke="var(--blue)"/>
      <line x1="498" y1="0" x2="660" y2="256" stroke="var(--teal)"/>
      <line x1="505" y1="0" x2="660" y2="245" stroke="var(--green)"/>
      <line x1="512" y1="0" x2="660" y2="234" stroke="var(--yellow)"/>
    </g>
  </svg>
  <div class="brand">
    <span class="brand__dot"></span>
    <span class="brand__name">Bright Horizon Painting and Remodeling</span>
  </div>
  <ul class="contact contact--phones">
    <li>
      <svg viewBox="0 0 16 16" aria-hidden="true"><path d="M3 1.5l3 3-1.6 1.8a9 9 0 0 0 5.3 5.3L11.5 10l3 3-1.8 2C7.5 15 1 8.5 1 3.3z" fill="var(--orange)"/></svg>
      (305) 555-0142
    </li>
    <li>
      <svg viewBox="0 0 16 16" aria-hidden="true"><rect x="4" y="1" width="8" height="5" fill="var(--pink)"/><rect x="1" y="6" width="14" height="7" rx="1.5" fill="var(--pink)"/><rect x="4" y="10" width="8" height="5" fill="#fff" stroke="var(--pink)"/></svg>
      (866) 555-0163
    </li>
    <li>
      <svg viewBox="0 0 16 16" aria-hidden="true"><path d="M2 5c0-2 2-3 6-3s6 1 6 3v2h-3V5H5v2H2zM3 8h10l1 6H2z" fill="var(--teal)"/></svg>
      Toll Free (855) 555-0197
    </li>
  </ul>
  <ul class="contact contact--web">
    <li>
      <svg viewBox="0 0 16 16" aria-hidden="true"><rect x="1" y="3" width="14" height="10" rx="1.5" fill="var(--green)"/><path d="M1.5 4l6.5 5 6.5-5" fill="none" stroke="#fff" stroke-width="1.3"/></svg>
      corinne@paintingbrighthorizon.example
    </li>
    <li>
      <svg viewBox="0 0 16 16" aria-hidden="true"><path d="M8 1a5 5 0 0 1 5 5c0 4-5 9-5 9S3 10 3 6a5 5 0 0 1 5-5z" fill="var(--gold)"/><circle cx="8" cy="6" r="1.8" fill="#fff"/></svg>
      4126 NW 71st st Suite 214, Miami, FL 33166
    </li>
  </ul>
</section>

</body>
</html>
```